Venture Capital Investment Firm

We are looking to overhaul our existing website (substantially), with only using the same logos (which we can provide).
We are an investment firm that focuses on making loans to late stage technology companies. Our site should ultimately look like other venture capital firms, and look modern and fresh. We have an existing website www.merrowfinch.com which this will be replacing, although we will be using a lot of the existing written content, and potentially the numbers of pages we will need, we are not wed to anything else. Please feel free to shoot any questions at any time and thank you in advance for your help!
Websites we like as examples:
https://www.tovalynbrook.com/
https://www.quenridgefund.com/
Target Market(s)
Potential investors who will invest in our firm, as well as potentially companies that are looking to borrow money from us.
Coding
Number of Pages Required
5+ page
Colors
Designer to choose colors to be used in the design.
Look and feel

```html
<!DOCTYPE html>
<html lang="en">
<head>
<meta charset="utf-8">
<title>Merrow Finch Investment Partners</title>
<link rel="stylesheet" href="https://fonts.googleapis.com/css2?family=Josefin+Sans:wght@400;600;700&family=Roboto:wght@400;500&display=swap">
<style>
:root{
  --red:#ec1c24;
  --navy:#1b1b4b;
  --grey:#d0d0d0;
  --white:#ffffff;
  --ink:#333333;
  --footer:#15131f;
  --hero-a:#1d2a3c;
  --hero-b:#4a5566;
}
*{box-sizing:border-box;margin:0;padding:0}
html,body{width:1200px;height:3443px;overflow:hidden}
body{position:relative;background:var(--grey);font-family:"Josefin Sans",sans-serif;color:var(--ink)}
.abs{position:absolute}
a{color:inherit}

/* header */
.site-header{left:0;top:0;width:1200px;height:76px;background:var(--white);border-bottom:1px solid #ddd}
.brand{left:73px;top:14px;display:flex;align-items:center;gap:12px}
.brand-dot{width:40px;height:40px;border-radius:50%;background:var(--navy)}
.brand-name{font-size:26px;font-weight:600;color:var(--navy);letter-spacing:1px}
.nav{left:355px;top:28px;display:flex;gap:36px;font-size:16px;color:var(--red);letter-spacing:.5px}
.btn{display:flex;align-items:center;justify-content:center;gap:10px;background:var(--red);color:var(--white);border-radius:5px;font-size:13px;letter-spacing:.5px}
.contact-btn{left:982px;top:17px;width:143px;height:39px}

/* hero */
.hero{left:0;top:76px;width:1200px;height:601px;background:linear-gradient(160deg,var(--hero-a) 0%,var(--hero-b) 55%,#6b5a52 100%)}
.hero-title{left:73px;top:222px;width:800px;font-size:27px;line-height:54px;color:var(--white);letter-spacing:.5px}
.hero-text{left:73px;top:396px;width:810px;font-size:13px;line-height:27px;color:var(--white);text-transform:uppercase}
.hero-btn-about{left:73px;top:557px;width:184px;height:48px}
.hero-btn-strategy{left:285px;top:557px;width:181px;height:48px;background:transparent;border:2px solid var(--red);color:var(--red)}

/* experience */
.section-title{font-size:32px;font-weight:700;color:var(--red);letter-spacing:1px}
.exp-title{left:74px;top:758px}
.stat-card{top:848px;width:262px;height:261px;background:var(--white);box-shadow:0 2px 6px rgba(0,0,0,.15);text-align:center;font-size:18px;font-weight:600;line-height:36px;letter-spacing:1px;color:#333}
.stat-card svg{display:block;margin:36px auto 14px}
.team-btn{left:138px;top:1144px;width:253px;height:46px}

/* callback */
.callback{left:76px;top:1344px;width:525px;height:600px;background:var(--white);box-shadow:0 2px 8px rgba(0,0,0,.2)}
.callback h2{position:absolute;top:42px;width:100%;text-align:center;font-size:30px;color:var(--red);font-weight:700}
.field{position:absolute;left:47px;width:430px;height:51px;border:2px solid #333;font-family:Roboto,sans-serif;font-size:17px;color:#777;padding:14px 24px}
.submit-btn{left:139px;top:490px;width:247px;height:50px;font-family:Roboto,sans-serif;font-size:19px}

/* testimonials */
.testimonials{left:601px;top:1390px;width:599px;height:507px;background:var(--white);border-top:1px solid #999;border-bottom:1px solid #999}
.testimonials h2{position:absolute;top:38px;width:100%;text-align:center;font-size:30px;color:var(--red);font-weight:700}
.quote-mark{font-family:Roboto,sans-serif;font-size:52px;color:#555;font-style:italic}
.quote-text{left:67px;top:112px;width:450px;font-family:Roboto,sans-serif;font-size:17px;line-height:27px;color:#333}
.avatar{left:184px;top:257px;width:106px;height:106px;border-radius:50%;border:2px solid var(--red);background:linear-gradient(#d8cfc6,#a99a8e)}
.reviewer{left:305px;top:272px;font-family:Roboto,sans-serif}
.stars{color:#e8c43c;font-size:17px;letter-spacing:2px}
.reviewer-name{font-size:22px;color:var(--navy)}
.reviewer-place{font-size:16px;color:#333}
.slider-nav{left:235px;top:425px}

/* news */
.news-frame{left:75px;top:2120px;width:1050px;height:590px;background:var(--white)}
.corner{border-color:var(--red);border-style:solid;width:80px;height:80px}
.corner-tl{left:55px;top:2098px;border-width:5px 0 0 5px}
.corner-br{left:1065px;top:2653px;border-width:0 5px 5px 0}
.news-title{left:94px;top:2148px}
.news-card{top:2227px;width:263px;height:337px;background:var(--white);border-radius:14px;box-shadow:0 2px 8px rgba(0,0,0,.18);overflow:hidden;text-align:center}
.news-meta{margin-top:12px;font-size:12px;color:var(--navy);display:flex;justify-content:center;gap:26px}
.news-card h3{margin:20px 10px 0;font-size:19px;line-height:27px;color:var(--red);font-weight:700}
.news-card p{margin:18px 16px 0;font-size:11.5px;line-height:18px;color:#444}
.news-read{position:absolute;left:0;bottom:0;width:100%;height:50px;background:var(--red);color:var(--white);font-size:14px;font-weight:700;display:flex;align-items:center;justify-content:center;letter-spacing:.5px}
.news-btn{left:136px;top:2612px;width:253px;height:48px}

/* footer */
.site-footer{left:0;top:2819px;width:1200px;height:624px;background:var(--footer);color:var(--white)}
.footer-heading{font-size:22px;font-weight:700;letter-spacing:1px}
.contact-list{left:122px;top:168px;font-size:12.5px;line-height:54px;letter-spacing:.3px}
.sitemap{left:450px;top:183px;font-size:13px;line-height:54px;letter-spacing:.5px}
.sitemap a{display:block;text-decoration:underline}
.social{left:733px;top:91px;display:flex;gap:50px}
.social span{width:40px;height:40px;border-radius:50%;background:var(--white)}
.footer-brand{left:688px;top:260px;display:flex;align-items:center;gap:18px}
.footer-brand .brand-dot{width:64px;height:64px;background:var(--white)}
.footer-brand-name{font-size:48px;font-weight:600;line-height:1}
.footer-brand-sub{font-size:15px;font-weight:600;letter-spacing:.5px;margin-top:6px}
.copyright{left:688px;top:470px;font-size:12px;text-decoration:underline}
</style>
</head>
<body>

<header class="site-header abs">
  <div class="brand abs"><span class="brand-dot"></span><span class="brand-name">MERROW FINCH</span></div>
  <nav class="nav abs"><span>HOME</span><span>STRATEGY</span><span>ABOUT US</span><span>TEAM</span><span>NEWS</span><span>INVESTORS</span></nav>
  <div class="btn contact-btn abs">CONTACT US</div>
</header>

<section class="hero abs" role="img" aria-label="Dusk photograph of glass skyscrapers in a financial district"></section>
<h1 class="hero-title abs" style="font-weight:400">WE ARE A GLOBAL STRUCTURED CREDIT INVESTMENT FIRM FOCUSED ON THE HEALTHCARE AND TECHNOLOGY INDUSTRIES</h1>
<p class="hero-text abs">Merrow Finch is a private investment firm unique in its dual focus on life science and technology credit opportunities. Our ambidextrous approach to investing reflects a broad recognition and appreciation for the critical role intellectual property plays in the successful commercialization of products. We apply our extensive industry expertise to assess the revenue visibility created by these assets and offer a range of creative financing solutions.</p>
<div class="btn hero-btn-about abs">ABOUT US</div>
<div class="btn hero-btn-strategy abs">OUR STRATEGY</div>

<h2 class="section-title exp-title abs">OUR EXPERIENCE</h2>
<div class="stat-card abs" style="left:138px">
  <svg width="100" height="100" viewBox="0 0 100 100" fill="none" stroke="#ec1c24" stroke-width="3"><line x1="50" y1="4" x2="50" y2="16"/><line x1="40" y1="8" x2="40" y2="16"/><line x1="60" y1="8" x2="60" y2="16"/><circle cx="50" cy="38" r="16"/><path d="M55 31h-8a4 4 0 0 0 0 8h6a4 4 0 0 1 0 8h-9M50 27v22"/><path d="M8 70h16v26H8zM24 74l20-4h14a4 4 0 0 1 0 8H44h22l22-12a5 5 0 0 1 6 8L66 92H24"/></svg>
  OVER $1.2B INVESTED<br><br>BY OUR PARTNERS.
</div>
<div class="stat-card abs" style="left:469px">
  <svg width="100" height="100" viewBox="0 0 100 100" fill="none" stroke="#ec1c24" stroke-width="3"><ellipse cx="50" cy="50" rx="44" ry="18"/><ellipse cx="50" cy="50" rx="44" ry="18" transform="rotate(60 50 50)"/><ellipse cx="50" cy="50" rx="44" ry="18" transform="rotate(-60 50 50)"/><circle cx="50" cy="50" r="6"/></svg>
  40+ LIFE SCIENCE<br>&amp; TECHNOLOGY<br>INVESTMENTS
</div>
<div class="stat-card abs" style="left:800px">
  <svg width="100" height="100" viewBox="0 0 100 100" fill="none" stroke="#ec1c24" stroke-width="3"><circle cx="70" cy="18" r="14"/><path d="M74 12h-6a3 3 0 0 0 0 6h4a3 3 0 0 1 0 6h-7M70 8v20"/><path d="M6 60l20-18 14 8 22-20"/><rect x="6" y="62" width="36" height="34"/><rect x="46" y="50" width="44" height="46"/><path d="M12 70h10v8H12zM26 70h10v8H26zM52 58h12v10H52zM70 58h12v10H70zM52 74h12v10H52zM70 74h12v10H70zM18 86h12v10H18z"/></svg>
  OVER A DECADE<br>INNOVATING<br>FINANCING STRUCTURES
</div>
<div class="btn team-btn abs">MEET OUR TEAM
  <svg width="44" height="12" viewBox="0 0 44 12" fill="none" stroke="#fff" stroke-width="2"><path d="M0 6h42M36 1l6 5-6 5"/></svg></div>

<section class="callback abs">
  <h2>Get a Callback</h2>
  <div class="field" style="top:115px">YOUR NAME</div>
  <div class="field" style="top:193px">YOUR EMAIL ADRESS</div>
  <div class="field" style="top:271px">CONTACT NUMBER</div>
  <div class="field" style="top:350px;height:111px">MESSAGE(OPTIONAL)</div>
  <div class="btn submit-btn abs">SUBMIT</div>
</section>

<section class="testimonials abs">
  <h2>TESTIMONIAL´S</h2>
  <span class="quote-mark abs" style="left:32px;top:70px">“</span>
  <p class="quote-text abs">Lorem ipsum dolor sit amet, consectetur adipiscing elit, sed do eiusmod tempor incididunt ut labore et dolore magna aliqua. Quis ipsum suspendisse ultrices gravida. Risus commodo viverra maecenas accumsan lacus vel facilisis.</p>
  <span class="quote-mark abs" style="left:520px;top:206px">”</span>
  <div class="avatar abs" role="img" aria-label="Portrait photo of the client"></div>
  <div class="reviewer abs">
    <div class="stars">★★★★</div>
    <div class="reviewer-name">JOHN DOE</div>
    <div class="reviewer-place">NYC, USA</div>
  </div>
  <svg class="slider-nav abs" width="128" height="60" viewBox="0 0 128 60" fill="none" stroke="#ec1c24" stroke-width="6" stroke-linecap="round"><path d="M28 4L6 30l22 26M100 4l22 26-22 26"/><circle cx="50" cy="30" r="3" fill="#ec1c24" stroke="none"/><circle cx="64" cy="30" r="3" fill="#1b1b4b" stroke="none"/><circle cx="78" cy="30" r="3" fill="#1b1b4b" stroke="none"/></svg>
</section>

<div class="corner corner-tl abs"></div>
<section class="news-frame abs"></section>
<div class="corner corner-br abs"></div>
<h2 class="section-title news-title abs">MERROW FINCH NEWS</h2>

<article class="news-card abs" style="left:134px">
  <div class="news-meta"><span>APRIL - 2018</span><span>Press Release</span></div>
  <h3>Merrow Finch completes structured debt investment in Brightlane</h3>
  <p>Merrow Finch Investment Partners ("Merrow Finch") announced today that it has completed a structured debt investment in Brightlane, Inc. ("Brightlane"), the leader in employee communication.</p>
  <div class="news-read">read full article</div>
</article>
<article class="news-card abs" style="left:469px">
  <div class="news-meta"><span>OCTOBER - 2016</span><span>Press Release</span></div>
  <h3>Merrow Finch completes $22,000,000 structured debt investment in Harbormint</h3>
  <p>Merrow Finch Investment Partners ("Merrow Finch") announced today that it has completed a $22,000,000 structured debt investment in Harbormint AS ("Harbormint"). Harbormint, headquartered in Oslo,</p>
  <div class="news-read">read full article</div>
</article>
<article class="news-card abs" style="left:803px">
  <div class="news-meta"><span>APRIL- 2016</span><span>PORTFOLIO NEWS</span></div>
  <h3>Corvane Semiconductor acquired by Lumetra for $55,000,000</h3>
  <p>Lumetra Optics, Inc., a leading supplier of advanced semiconductor communications components for use in Cloud connectivity, data centers, and high-speed optical and wireless networks, today announced the signing</p>
  <div class="news-read">read full article</div>
</article>
<div class="btn news-btn abs">READ MORE NEWS
  <svg width="44" height="12" viewBox="0 0 44 12" fill="none" stroke="#fff" stroke-width="2"><path d="M0 6h42M36 1l6 5-6 5"/></svg></div>

<footer class="site-footer abs">
  <h3 class="footer-heading abs" style="left:123px;top:94px">CONTACT US</h3>
  <div class="contact-list abs">
    <div>GENERAL INQUIRIES</div>
    <div>Please write to: &nbsp;inquiries@merrowfinch.com</div>
    <div>MEDIA INQUIRIES</div>
    <div>Please write to: &nbsp;media@merrowfinch.com</div>
    <div>ADRESS:</div>
    <div>2200 Alder Row #310</div>
    <div>Fairhaven, CA &nbsp;94088</div>
  </div>
  <h3 class="footer-heading abs" style="left:450px;top:94px">SITEMAP</h3>
  <nav class="sitemap abs"><a>HOME</a><a>STRATEGY</a><a>ABOUT US</a><a>TEAM</a><a>NEWS</a><a>INVESTORS</a></nav>
  <div class="social abs" aria-label="Social media links"><span></span><span></span><span></span><span></span></div>
  <div class="footer-brand abs">
    <span class="brand-dot"></span>
    <div><div class="footer-brand-name">MERROW FINCH</div><div class="footer-brand-sub">INVESTMENT PARTNERS, LLC</div></div>
  </div>
  <div class="copyright abs">© 2015 Merrow Finch Investment Partners LLC. &nbsp;All Rights Reserved.</div>
</footer>

</body>
</html>
```